Business Card Design

Need a hot business card in wine colors something cool and mod please feel free to be , FUNKY and free with this .

Industry/Entity Type

Business

Contact Information for Business Card

LUMERA HAIR DESIGN 3182 w 9th st scottsdale az 85619 Custom modern hair design and custom color by MARCUS OBRIDGE 602-4168203 cell salon 480 -712-6084 email marcusobridge@quillpost.com hours wed thru sat 7am to 6pm.

Font styles to use
Other font styles liked:
• something fun and mod.

Colors
a54599
6b449b
1b1b1b
606060

Requirements
Must have
• Apointment reminder on flip side of card.
Should not have
• Nothing boring.

```html
<!DOCTYPE html>
<html lang="en">
<head>
<meta charset="utf-8">
<title>Lumera Hair Design – Business Card</title>
<link rel="stylesheet" href="https://fonts.googleapis.com/css2?family=Sorts+Mill+Goudy:ital@0;1&family=Montserrat:wght@700&display=swap">
<style>
  :root {
    --canvas-bg: #e9e6ec;
    --card-purple: #7b58a9;
    --card-purple-deep: #6b449b;
    --ink-dark: #1b1b1b;
    --ink-light: #ffffff;
    --hair-dark: #121214;
    --hair-mid: #2e2e33;
    --hair-shine: #5a5a62;
  }
  * { box-sizing: border-box; margin: 0; padding: 0; }
  html, body {
    width: 1200px;
    height: 1000px;
    overflow: hidden;
    background: var(--canvas-bg);
  }
  .canvas {
    position: relative;
    width: 1200px;
    height: 1000px;
  }
  .card {
    position: absolute;
    top: 168px;
    width: 380px;
    height: 664px;
    border-radius: 4px;
    overflow: hidden;
    box-shadow: 0 10px 28px rgba(0,0,0,0.18);
  }
  .card--front { left: 170px; }
  .card--back {
    left: 650px;
    background: linear-gradient(160deg, var(--card-purple) 0%, var(--card-purple-deep) 100%);
    font-family: "Sorts Mill Goudy", Georgia, serif;
    color: var(--ink-dark);
    text-align: right;
    padding: 0 30px;
  }
  .hair-photo {
    width: 100%;
    height: 100%;
    background:
      linear-gradient(100deg, transparent 30%, rgba(255,255,255,0.10) 45%, transparent 60%),
      linear-gradient(180deg, var(--hair-mid) 0%, var(--hair-dark) 35%, var(--hair-shine) 60%, var(--hair-dark) 100%);
  }
  .reminder {
    position: absolute;
    left: 24px;
    right: 24px;
    bottom: 24px;
    padding: 14px 18px;
    background: rgba(107,68,155,0.88);
    color: var(--ink-light);
    font-family: "Sorts Mill Goudy", Georgia, serif;
    border-radius: 3px;
  }
  .reminder__title {
    font-family: "Montserrat", Arial, sans-serif;
    font-weight: 700;
    font-size: 15px;
    letter-spacing: 1px;
    margin-bottom: 8px;
  }
  .reminder__line {
    font-size: 16px;
    line-height: 1.7;
  }
  .reminder__hours {
    font-style: italic;
    font-size: 14px;
    margin-top: 6px;
  }
  .brand {
    margin-top: 110px;
    display: flex;
    flex-direction: column;
    align-items: flex-end;
  }
  .brand__mark {
    width: 34px;
    height: 34px;
    border-radius: 50%;
    background: var(--ink-light);
    position: absolute;
    top: 40px;
    left: 30px;
  }
  .brand__name {
    font-size: 74px;
    line-height: 1;
    color: var(--ink-light);
    letter-spacing: 1px;
  }
  .brand__tag {
    font-family: "Montserrat", Arial, sans-serif;
    font-weight: 700;
    font-size: 27px;
    letter-spacing: 0.5px;
    color: var(--ink-dark);
    margin-top: 2px;
  }
  .credit {
    margin-top: 40px;
    font-style: italic;
    font-size: 19px;
    line-height: 1.2;
    text-align: center;
    padding-left: 40px;
  }
  .stylist {
    font-size: 29px;
    font-weight: 400;
    letter-spacing: 1px;
    color: var(--ink-light);
    margin-top: 8px;
    text-align: right;
    white-space: nowrap;
  }
  .address {
    margin-top: 26px;
    font-style: normal;
    font-size: 18px;
    line-height: 1.3;
    text-align: center;
  }
  .address__salon { font-size: 20px; letter-spacing: 0.5px; }
  .contact {
    margin-top: 24px;
    font-size: 17px;
    line-height: 1.35;
    text-align: center;
    white-space: nowrap;
  }
</style>
</head>
<body>
<main class="canvas">
  <section class="card card--front">
    <div class="hair-photo" role="img" aria-label="Photograph of a model with long, straight, glossy black hair and a fringe"></div>
    <div class="reminder">
      <p class="reminder__title">APPOINTMENT REMINDER</p>
      <p class="reminder__line">Date: ____________________</p>
      <p class="reminder__line">Time: ____________________</p>
      <p class="reminder__hours">Hours: Wed thru Sat, 7am to 6pm</p>
    </div>
  </section>

  <section class="card card--back">
    <span class="brand__mark" aria-hidden="true"></span>
    <header class="brand">
      <span class="brand__name">Lumera</span>
      <span class="brand__tag">HAIR DESIGN</span>
    </header>

    <p class="credit">Custom Modern Hair<br>Design &amp; Custom Color By:</p>
    <h1 class="stylist">MARCUS OBRIDGE</h1>

    <address class="address">
      <span class="address__salon">LUMERA HAIR DESIGN</span><br>
      3182 W 9th St, Scottsdale,<br>
      AZ 85619.
    </address>

    <p class="contact">
      Cell: 602-4168203<br>
      Salon: 480 -712-6084<br>
      Email: marcusobridge@quillpost.com
    </p>
  </section>
</main>
</body>
</html>
```